6' Banner Stands for exhibiting to Health Fairs with an audience of age 55+

We need designs for two 6' banner stands to stand on either side of our exhibition tables. We offer Hereditary Cancer Screening. I want the banners to have the same look and feel as the logo and the files color scheme logo, etc..

The Banners should have "Hereditary Cancer Screening" at the top with the Tag Line "The Test You Take For Them" underneath. A photo of grandparents with kids/grandkids and underneath the photos in large font one of the following messages:
1) "A Simple Swab Could Save A Family Members LIFE Get Tested Today!"
2) "Does Cancer Run In Your Family? Get Tested Today!"
3) "Knowledge Is Power" "Get Tested Today!"
4) "Will You Give Your Loved Ones The Information To Beat Cancer In Their Lives? Get Tested Today!
5) Knowledge Is Power Get Tested Today!"
Updates

Thank you all for your designs I now have the exact specs for the banners, so please use these as you update your designs. 31.5 inches X 83.25 inches and add a 1/2 inch bleed to all 4 sides. Thank you.

Target Market(s)

Persons 55+ who are grandparents

Industry/Entity Type

Healthcare

Font styles to use
Sans Serif
Other font styles liked:
• Comic Sans for "The Test You Take For Them"

Colors
9bcb3c
0356a4
ffffff

Requirements
Must have
• the main focus should be the hereditary cancer screening; "Hereditary Cancer Screening";
• "The test you order for them" in Comic Sans font underneath
• A photo or photos of grandparents with their grandchildren (multiple ethnicities)
• One of the slogans listed above
• GET TESTED TODAY underneath the messages at the bottom of the banner highlighted and eye catching
• www.kinhealthcheckup.net
Nice to have
• Logo at the top or bottom

```html
<!DOCTYPE html>
<html lang="en">
<head>
<meta charset="utf-8">
<title>Hereditary Cancer Screening – Banner Stands</title>
<link href="https://fonts.googleapis.com/css2?family=Jost:wght@400;500;700;800&family=Comic+Neue:wght@400;700&display=swap" rel="stylesheet">
<style>
  :root{
    --board:#b9babc;
    --navy:#0a2a6e;
    --blue:#0356a4;
    --blue-deep:#071f5c;
    --green:#9bcb3c;
    --white:#ffffff;
    --ink:#111111;
    --photo-warm:#c9a98c;
    --photo-light:#dcd4c8;
  }
  *{box-sizing:border-box;margin:0;padding:0}
  html,body{width:1174px;height:1200px;overflow:hidden;background:var(--board)}
  .board{position:absolute;left:0;top:0;width:1200px;height:1227px;transform:scale(0.97833);transform-origin:0 0;background:var(--board);font-family:"Jost",sans-serif}
  .banner{position:absolute;top:61px;width:415px;height:964px;background:var(--white);overflow:hidden}
  .banner--knowledge{left:146px}
  .banner--family{left:638px}
  .banner svg.shapes{position:absolute;left:0;top:0;width:415px;height:964px}
  .brand{position:absolute;top:24px;left:128px;display:flex;align-items:center;gap:8px}
  .brand__dot{width:58px;height:58px;border-radius:50%;background:var(--navy)}
  .brand__name{font-weight:700;font-size:19px;line-height:19px;color:var(--navy);letter-spacing:.5px;text-transform:uppercase}
  .ribbon{position:absolute;border-radius:30px 30px 6px 6px;background:linear-gradient(135deg,#c48bc4,#6fb7e0)}
  .line{position:absolute;left:0;width:100%;text-align:center;line-height:1;white-space:nowrap}
  .title{color:var(--white);font-weight:500;letter-spacing:2px}
  .title--sm{font-size:50px}
  .title--lg{font-size:68px}
  .divider{position:absolute;height:3px;background:var(--white)}
  .tagline{font-family:"Comic Neue",sans-serif;font-weight:400;font-size:27px;color:var(--green)}
  .photo{position:absolute}
  .cta{position:absolute;border-radius:50%;background:var(--green);display:flex;flex-direction:column;justify-content:center;align-items:center;color:var(--white);font-weight:700;line-height:1.05;text-align:center}
  .thumb{position:absolute;border-radius:50%;border:5px solid var(--green);background:radial-gradient(circle,var(--photo-warm),#6e5a46)}
  .slogan{font-weight:800;color:var(--green);font-size:34px;letter-spacing:1.5px}
  .question{font-weight:800;color:var(--blue);font-size:32px;letter-spacing:1.5px}
  .url{color:var(--white);font-size:20px;font-weight:400}
  .card{position:absolute;left:27px;top:344px;width:359px;height:298px;border-radius:30px;background:linear-gradient(135deg,var(--blue),var(--blue-deep))}
  .caption{position:absolute;left:0;top:1112px;width:1200px;text-align:center;font-size:64px;font-weight:400;color:var(--ink);letter-spacing:4px}
</style>
</head>
<body>
<main class="board">

  <!-- Banner: Knowledge Is Power -->
  <section class="banner banner--knowledge">
    <svg class="shapes" viewBox="0 0 415 964" aria-hidden="true">
      <defs>
        <linearGradient id="navyFill" x1="0" y1="0" x2="0" y2="1">
          <stop offset="0" stop-color="#071f5c"/><stop offset="1" stop-color="#0356a4"/>
        </linearGradient>
      </defs>
      <path d="M0 58 Q200 95 415 70 L415 98 Q200 118 0 82 Z" fill="var(--green)"/>
      <path d="M0 80 Q200 116 415 96 L415 428 Q200 470 0 418 Z" fill="url(#navyFill)"/>
      <path d="M0 768 Q200 710 415 728 L415 964 L0 964 Z" fill="var(--green)"/>
      <path d="M0 790 Q200 738 415 752 L415 964 L0 964 Z" fill="url(#navyFill)"/>
    </svg>
    <div class="photo" role="img" aria-label="Photo of smiling grandparents with their adult children and grandchildren outdoors"
         style="left:0;top:420px;width:415px;height:340px;background:linear-gradient(180deg,#a8b58a,var(--photo-warm) 45%,var(--photo-light));clip-path:path('M0 0 Q200 48 415 8 L415 310 Q200 292 0 350 Z')"></div>
    <div class="brand"><span class="brand__dot"></span><span class="brand__name">Kinwell<br>Health<br>Group</span></div>
    <div class="ribbon" role="img" aria-label="Awareness ribbon" style="left:188px;top:92px;width:42px;height:92px"></div>
    <div class="line title title--sm" style="top:187px">HEREDITARY</div>
    <div class="line title title--lg" style="top:233px">CANCER</div>
    <div class="line title title--sm" style="top:295px">SCREENING</div>
    <div class="divider" style="left:149px;top:364px;width:115px"></div>
    <div class="line tagline" style="top:380px">“The Test You Take</div>
    <div class="line tagline" style="top:411px">For Them”</div>
    <div class="cta" style="left:125px;top:685px;width:154px;height:154px;font-size:31px"><span>Get</span><span>Tested</span><span>Today!</span></div>
    <div class="line slogan" style="top:848px">KNOWLEDGE</div>
    <div class="line slogan" style="top:880px">IS POWER</div>
    <div class="line url" style="top:916px">www.kinhealthcheckup.net</div>
  </section>

  <!-- Banner: Does Cancer Run In Your Family -->
  <section class="banner banner--family">
    <svg class="shapes" viewBox="0 0 415 964" aria-hidden="true">
      <path d="M0 70 Q200 95 415 62 L415 86 Q200 120 0 92 Z" fill="var(--blue)"/>
      <path d="M0 92 Q200 122 415 86 L415 104 Q200 142 0 112 Z" fill="var(--green)"/>
      <path d="M0 832 Q200 790 415 770 L415 964 L0 964 Z" fill="var(--green)"/>
      <path d="M0 852 Q200 810 415 792 L415 964 L0 964 Z" fill="var(--blue)"/>
    </svg>
    <div class="photo" role="img" aria-label="Photo of laughing grandparents playing with their grandchildren"
         style="left:0;top:100px;width:415px;height:320px;background:linear-gradient(180deg,var(--photo-light),var(--photo-warm) 55%,#ffffff);clip-path:path('M0 22 Q200 52 415 4 L415 320 L0 320 Z')"></div>
    <div class="brand"><span class="brand__dot"></span><span class="brand__name">Kinwell<br>Health<br>Group</span></div>
    <div class="card"></div>
    <div class="ribbon" role="img" aria-label="Awareness ribbon" style="left:180px;top:266px;width:50px;height:106px"></div>
    <div class="line title title--sm" style="top:377px">HEREDITARY</div>
    <div class="line title title--lg" style="top:423px">CANCER</div>
    <div class="line title title--sm" style="top:485px">SCREENING</div>
    <div class="divider" style="left:150px;top:553px;width:115px"></div>
    <div class="line tagline" style="top:568px">“The Test You Take</div>
    <div class="line tagline" style="top:600px">For Them”</div>
    <div class="line question" style="top:658px">DOES CANCER</div>
    <div class="line tagline" style="top:692px;font-size:29px">Run In Your Family?</div>
    <div class="thumb" role="img" aria-label="Photo of a grandparent's hand holding a child's hand" style="left:30px;top:799px;width:92px;height:92px"></div>
    <div class="thumb" role="img" aria-label="Photo of a smiling grandmother hugging her grandchild" style="left:292px;top:740px;width:94px;height:94px"></div>
    <div class="cta" style="left:143px;top:734px;width:124px;height:124px;font-size:28px"><span>Get</span><span>Tested</span><span>Today!</span></div>
    <div class="line url" style="top:906px">www.kinhealthcheckup.net</div>
  </section>

  <div class="caption">OTHER DESIGN OPTION</div>
</main>
</body>
</html>
```